Web site for a company that sells Pinball machines

We need a website that is an online shopping experience for a Store that sells pinball machines and accessories. The name of the store is called "Bumper Vault Arcade." The store it self has a showroom, but we would also like to have an Internet e-commerce presence. We pinball machines made by Halvern gameworks. You can visit their website and see their current list of machines as well as their website for the machines that we are going to carry in our store. Their website is Halverngameworks.example. I am able to use their machine photos as well as their machine brochure PDF files. I am also able to use their logo on my website two list it as a Halvern Authorized Dealer.
This website design needs to be funky, fun, very technologically oriented and modern. The people buying machines our spending anywhere between $5000 and $15,000 on one machine. These Are high-end buyers who are also usually fairly tech savvy or at least enjoy technology and graphics.
Attachments: I have attached photographs of some of my own machines which may be used in the website. I've also attached some downloaded files from Halvern gameworks.example as well as some of their PDF files for brochures. I will carry all of their current models they have listed under games. Not the archived games. I have included one of their machines called Copperfield Limited edition in my photograph attachments. The rest of the photos are just random pictures that I have taken myself and maybe used to build the site. Lastly I have attached my logo which I am not super crazy about so I will also be posting a contest to redesign this logo. Tons more of my own pinball photos are available.
I would like for people to be able to purchase machines and accessories from the website, but also inform them to our actual showroom.
Updates
Target Market(s)
Target market is 16 to 75. Techy individuals to enjoy gaming technology video animation and Vegas style twinkle
Industry/Entity Type
It Company
Coding
Coded - Design and coding required
Number of Pages Required
3 page
Look and feel

```html
<!DOCTYPE html>
<html lang="en">
<head>
<meta charset="utf-8">
<title>Bumper Vault Arcade</title>
<link href="https://fonts.googleapis.com/css2?family=Roboto:wght@400;500;700;900&display=swap" rel="stylesheet">
<style>
:root{
  --space:#0c1424;
  --space-deep:#070b16;
  --red:#b52a05;
  --red-bright:#d23a0c;
  --red-deep:#8f1d02;
  --ink:#1a1a1a;
  --paper:#f4f3f3;
  --card:#f7f5f5;
  --grey:#d6d4d4;
  --text:#333;
  --star:#c00;
  --gold:#f4c20d;
  --white:#fff;
}
*{margin:0;padding:0;box-sizing:border-box}
html,body{width:1200px;height:2643px;overflow:hidden}
body{font-family:'Roboto',sans-serif;background:radial-gradient(ellipse at 50% 40%,#16233a 0%,var(--space) 55%,var(--space-deep) 100%);position:relative;color:var(--text)}
.abs{position:absolute}
svg{display:block}

/* top bar */
.topbar{left:0;top:21px;width:1200px;height:37px;background:var(--red);color:var(--white);font-size:13px;display:flex;align-items:center}
.topbar .contact{position:absolute;left:88px;display:flex;gap:30px;align-items:center}
.topbar .contact span{display:flex;align-items:center;gap:7px}
.topbar .account{position:absolute;left:987px;display:flex;gap:8px;align-items:center}

/* header */
.header{left:0;top:58px;width:1200px;height:109px;background:rgba(10,16,28,.85)}
.brand{left:88px;top:22px;display:flex;align-items:center;gap:10px}
.brand .mark{width:22px;height:22px;border-radius:50%;background:var(--red-bright)}
.brand .name{font-size:20px;font-weight:700;color:var(--white);width:120px;line-height:1.15}
.search{left:749px;top:58px;width:365px;height:29px;display:flex}
.search .field{flex:1;background:var(--white);font-size:11px;color:#999;padding:8px 10px}
.search .btn{width:48px;background:var(--space);border:1px solid var(--white)}
.cart{left:1082px;top:16px}
.cart .count{position:absolute;left:14px;top:-6px;width:16px;height:16px;border-radius:50%;background:var(--gold);font-size:8px;color:var(--ink);text-align:center;line-height:16px}

/* nav */
.nav{left:0;top:167px;width:1200px;height:37px;background:var(--red);border-bottom:2px solid var(--red-deep)}
.nav a{position:absolute;top:11px;color:var(--white);font-size:13px;font-weight:700;text-decoration:none}

/* hero */
.hero{left:0;top:204px;width:1200px;height:414px;background:radial-gradient(circle at 80% 40%,#4d7aa8 0%,#2e4f7a 18%,transparent 32%),radial-gradient(circle at 30% 55%,#e5a16c 0%,#c7442a 35%,transparent 60%),linear-gradient(110deg,#d9663b 0%,#b73a1e 40%,#d88c5a 60%,#a23018 100%)}
.hero-copy{left:109px;top:302px}
.hero-copy .kicker{font-size:46px;font-weight:700;color:var(--red-deep);line-height:1}
.hero-copy .offer{font-size:82px;font-weight:900;color:var(--ink);line-height:1;margin-top:6px}
.hero-copy p{font-size:14px;font-weight:700;color:var(--ink);line-height:24px;margin-top:4px;width:340px;letter-spacing:.9px}
.shop-now{left:111px;top:507px;width:145px;height:36px;border-radius:18px;background:var(--ink);color:var(--white);font-size:13px;font-weight:700;text-align:center;line-height:36px}
.slider-arrows{left:974px;top:204px;width:140px;height:51px;background:var(--ink);border-bottom-left-radius:14px;display:flex;justify-content:center;gap:30px;align-items:center}

/* products */
.products{left:86px;top:618px;width:1028px;height:510px;background:var(--paper)}
.tabs{left:86px;top:641px;width:1028px;height:46px;background:#050505;color:var(--white)}
.tabs span{position:absolute;top:14px;font-size:16px}
.tabs .dim{color:#aaa}
.tabs .on{font-weight:700}
.tab-sep{top:12px;color:#aaa}
.card-top{width:225px;top:712px}
.card-top .tag{height:37px;background:var(--red);color:var(--white);font-size:17px;text-align:center;line-height:37px}
.card-top .photo{height:247px}
.card-top .title{font-size:17px;color:var(--ink);margin:12px 0 0 8px}
.price{font-size:16px;color:var(--red)}
.price s{color:#888;margin-right:4px}
.card-top .price{margin:6px 0 0 8px}
.stars{margin:5px 0 0 8px;display:flex;gap:3px}
.stars svg{width:9px;height:9px}
.pill{display:inline-block;background:#444;color:var(--white);font-size:8px;font-weight:700;border-radius:8px;padding:3px 10px;margin:8px 0 0 8px}

/* arrivals */
.arrivals{left:86px;top:1128px;width:1028px;height:749px;background:var(--grey)}
.section-head{width:1200px;left:0;text-align:center;font-size:28px;font-weight:500;color:#2b2b2b}
.rule{height:2px;width:48px;background:#888;left:576px}
.card-arr{width:226px;height:269px;background:var(--card)}
.card-arr .photo{height:162px;position:relative}
.badge{position:absolute;right:0;top:0;background:var(--gold);color:var(--ink);font-size:14px;padding:3px 10px}
.card-arr .title{text-align:center;font-size:18px;color:var(--ink);margin-top:16px}
.card-arr .price{text-align:center;margin-top:4px}
.card-arr .btn{display:block;width:66px;margin:8px auto 0;background:var(--red);color:var(--white);font-size:8px;font-weight:700;text-align:center;padding:4px 0}
.pager{width:86px;height:30px;border-radius:15px;background:#444;border:1px solid #222;display:flex;align-items:center;justify-content:center;top:1824px}

/* blogs */
.blogs{left:86px;top:1877px;width:1028px;height:373px;background:radial-gradient(ellipse at 50% 60%,#e2502a 0%,var(--red-bright) 45%,var(--red-deep) 100%)}
.blog{width:308px;top:1963px;color:var(--white)}
.blog .photo{height:148px}
.blog h3{font-size:21px;font-weight:500;margin-top:12px}
.blog p{font-size:11px;line-height:16px;margin-top:8px;opacity:.9}
.blog .meta{display:flex;gap:18px;font-size:11px;font-style:italic;margin-top:10px;align-items:center}
.blog .meta span{display:flex;gap:6px;align-items:center}

/* social */
.social{top:2266px;width:36px;height:36px;border-radius:50%;background:var(--white)}

/* footer */
.footer{left:0;top:2313px;width:1200px;height:283px;background:linear-gradient(180deg,#efecec,#dcd8d8)}
.footer-brand{left:146px;top:2380px;display:flex;align-items:center;gap:10px}
.footer-brand .mark{width:20px;height:20px;border-radius:50%;background:var(--red)}
.footer-brand .name{font-size:19px;font-weight:700;color:var(--ink);width:120px;line-height:1.15}
.footer-addr{left:152px;top:2488px;display:flex;gap:12px;font-size:13px;line-height:16px;color:#333;width:180px}
.footer-phone{left:152px;top:2545px;display:flex;gap:12px;font-size:14px;font-weight:700;color:#222;align-items:center}
.vline{width:1px;height:168px;background:#555;top:2375px}
.f-head{top:2353px;font-size:14px;color:#333}
.f-list{list-style:none;font-size:11px;color:#333}
.f-list li{display:flex;gap:10px;align-items:center;height:31px}
.f-blog{display:flex;gap:8px;width:220px;height:49px}
.f-blog .thumb{width:46px;height:34px;flex:none;background:linear-gradient(135deg,#5b2a6e,#c14b2a,#e2b23a)}
.f-blog p{font-size:9px;line-height:11px;color:#333}
.f-blog small{display:block;font-size:7px;color:#777;margin-top:2px}
.basebar{left:0;top:2596px;width:1200px;height:47px;background:#0a0a0d}
</style>
</head>
<body>

<svg width="0" height="0" style="position:absolute">
  <symbol id="star-full" viewBox="0 0 9 9"><path d="M4.5 0l1.1 3.2H9L6.3 5.2l1 3.3-2.8-2-2.8 2 1-3.3L0 3.2h3.4z" fill="#c00"/></symbol>
  <symbol id="star-empty" viewBox="0 0 9 9"><path d="M4.5 .8l.9 2.7h2.8L5.9 5.2l.9 2.6-2.3-1.6-2.3 1.6.9-2.6L.8 3.5h2.8z" fill="none" stroke="#c00" stroke-width=".8"/></symbol>
</svg>

<!-- top bar -->
<div class="abs topbar">
  <div class="contact">
    <span><svg width="11" height="11" viewBox="0 0 24 24"><path fill="#fff" d="M6.6 10.8a15 15 0 006.6 6.6l2.2-2.2c.3-.3.7-.4 1-.2 1.1.4 2.3.6 3.6.6.6 0 1 .4 1 1V20c0 .6-.4 1-1 1A17 17 0 013 4c0-.6.4-1 1-1h3.5c.6 0 1 .4 1 1 0 1.3.2 2.5.6 3.6.1.3 0 .7-.2 1z"/></svg>(+000) 555 010 0199</span>
    <span><svg width="13" height="10" viewBox="0 0 26 20"><rect width="26" height="20" fill="#fff"/><path d="M0 0l13 10L26 0" stroke="#b52a05" stroke-width="2" fill="none"/></svg>24X7 Customer Care</span>
  </div>
  <div class="account">
    <svg width="10" height="10" viewBox="0 0 10 10"><rect x=".5" y=".5" width="9" height="9" fill="none" stroke="#fff"/><path d="M2 5h5M5 3l2 2-2 2" stroke="#fff" fill="none"/></svg>
    <span>Login</span><span>|</span><span>Register</span>
  </div>
</div>

<!-- header -->
<div class="abs header">
  <div class="abs brand"><div class="mark"></div><div class="name">Bumper Vault Arcade</div></div>
  <div class="abs search"><div class="field">Search...</div><div class="btn"></div></div>
  <div class="abs cart">
    <svg width="22" height="20" viewBox="0 0 22 20"><path d="M1 2h4l3 10h10l3-7H7" stroke="#fff" stroke-width="2" fill="none"/><circle cx="9" cy="16" r="2" fill="#fff"/><circle cx="17" cy="16" r="2" fill="#fff"/></svg>
    <div class="count">01</div>
  </div>
</div>

<!-- nav -->
<nav class="abs nav">
  <a style="left:268px">HOME</a>
  <a style="left:368px">ABOUT US</a>
  <a style="left:493px">GAMES</a>
  <a style="left:599px">COMMUNITY</a>
  <a style="left:740px">SUPPORT</a>
  <a style="left:862px">CONTACT US</a>
</nav>

<!-- hero -->
<section class="abs hero" role="img" aria-label="Close-up photo of a lit pinball playfield with bumpers and posts"></section>
<div class="abs hero-copy">
  <div class="kicker">LOREM IPSUM</div>
  <div class="offer">40% OFF</div>
  <p>It is a long established fact that a reader will be distracted by the readable content.</p>
</div>
<div class="abs shop-now">SHOP NOW</div>
<div class="abs slider-arrows">
  <svg width="14" height="24" viewBox="0 0 14 24"><path d="M12 2L2 12l10 10" stroke="#fff" stroke-width="2" fill="none"/></svg>
  <svg width="14" height="24" viewBox="0 0 14 24"><path d="M2 2l10 10L2 22" stroke="#fff" stroke-width="2" fill="none"/></svg>
</div>

<!-- featured products -->
<section class="abs products"></section>
<div class="abs tabs">
  <span class="dim" style="left:25px">BEST SELLING</span>
  <span class="tab-sep" style="left:191px">|</span>
  <span class="on" style="left:242px">FEATURE</span>
  <span class="tab-sep" style="left:365px">|</span>
  <span class="on" style="left:416px">POPULAR</span>
  <span style="left:901px;font-size:14px;top:15px">VIEW ALL &#187;</span>
</div>

<div class="abs card-top" style="left:111px">
  <div class="tag">PINBALL</div>
  <div class="photo" role="img" aria-label="Pinball machine playfield artwork" style="background:linear-gradient(150deg,#3b4fa0,#c23c5a,#e4b03a,#2f6f4a)"></div>
  <div class="title">Flipside Comet</div>
  <div class="price"><s>$10.00</s>$8.00</div>
  <div class="stars"><svg><use href="#star-full"/></svg><svg><use href="#star-full"/></svg><svg><use href="#star-full"/></svg><svg><use href="#star-full"/></svg><svg><use href="#star-empty"/></svg></div>
  <div class="pill">Add to Cart</div>
</div>
<div class="abs card-top" style="left:361px">
  <div class="tag">PINBALL</div>
  <div class="photo" role="img" aria-label="Pinball playfield with flippers and star artwork" style="background:linear-gradient(160deg,#e8c23a,#c8482a,#1f2f5a)"></div>
  <div class="title">Flipside Comet</div>
  <div class="price"><s>$10.00</s>$8.00</div>
  <div class="stars"><svg><use href="#star-full"/></svg><svg><use href="#star-full"/></svg><svg><use href="#star-full"/></svg><svg><use href="#star-full"/></svg><svg><use href="#star-empty"/></svg></div>
  <div class="pill">Add to Cart</div>
</div>
<div class="abs card-top" style="left:611px">
  <div class="tag">PINBALL</div>
  <div class="photo" role="img" aria-label="Pinball playfield ramps under purple lighting" style="background:linear-gradient(150deg,#6a3fa0,#2e2f6a,#4aa07a,#c94c8a)"></div>
  <div class="title">Flipside Comet</div>
  <div class="price"><s>$10.00</s>$8.00</div>
  <div class="stars"><svg><use href="#star-full"/></svg><svg><use href="#star-full"/></svg><svg><use href="#star-full"/></svg><svg><use href="#star-full"/></svg><svg><use href="#star-empty"/></svg></div>
  <div class="pill">Add to Cart</div>
</div>
<div class="abs card-top" style="left:863px">
  <div class="tag">PINBALL</div>
  <div class="photo" role="img" aria-label="Red pinball cabinet coin door" style="background:linear-gradient(160deg,#c2281e,#8a1410,#d8b45a)"></div>
  <div class="title">Flipside Comet</div>
  <div class="price"><s>$10.00</s>$8.00</div>
  <div class="stars"><svg><use href="#star-full"/></svg><svg><use href="#star-full"/></svg><svg><use href="#star-full"/></svg><svg><use href="#star-full"/></svg><svg><use href="#star-empty"/></svg></div>
  <div class="pill">Add to Cart</div>
</div>

<!-- recent arrivals -->
<section class="abs arrivals"></section>
<h2 class="abs section-head" style="top:1156px">RECENT ARRIVALS TO OUR STORE</h2>
<div class="abs rule" style="top:1206px"></div>

<div class="abs card-arr" style="left:111px;top:1234px"><div class="photo" role="img" aria-label="Pinball playfield artwork" style="background:linear-gradient(150deg,#3b4fa0,#c9a23a,#6a3a7a)"></div><div class="title">Flipside Comet</div><div class="price"><s>$10.00</s>$8.00</div><span class="btn">Add to Cart</span></div>
<div class="abs card-arr" style="left:361px;top:1234px"><div class="photo" role="img" aria-label="Row of pinball machines in a showroom" style="background:linear-gradient(150deg,#8a2a4a,#3a3a6a,#c46a8a)"><span class="badge">Sale!</span></div><div class="title">Flipside Comet</div><div class="price"><s>$10.00</s>$8.00</div><span class="btn">Add to Cart</span></div>
<div class="abs card-arr" style="left:611px;top:1234px"><div class="photo" role="img" aria-label="Colourful pinball playfield" style="background:linear-gradient(150deg,#e0b43a,#c8482a,#2f4f8a)"><span class="badge" style="background:var(--red);color:#fff">Off!</span></div><div class="title">Flipside Comet</div><div class="price"><s>$10.00</s>$8.00</div><span class="btn">Add to Cart</span></div>
<div class="abs card-arr" style="left:863px;top:1234px"><div class="photo" role="img" aria-label="Red pinball cabinet coin door" style="background:linear-gradient(160deg,#c2281e,#8a1410,#d8b45a)"></div><div class="title">Flipside Comet</div><div class="price"><s>$10.00</s>$8.00</div><span class="btn">Add to Cart</span></div>

<div class="abs card-arr" style="left:111px;top:1528px"><div class="photo" role="img" aria-label="Pinball playfield ramps under purple lighting" style="background:linear-gradient(150deg,#6a3fa0,#2e2f6a,#4aa07a)"></div><div class="title">Flipside Comet</div><div class="price"><s>$10.00</s>$8.00</div><span class="btn">Add to Cart</span></div>
<div class="abs card-arr" style="left:361px;top:1528px"><div class="photo" role="img" aria-label="Pinball playfield with yellow value insert" style="background:linear-gradient(150deg,#5a3a8a,#3a5aa0,#e8c83a)"></div><div class="title">Flipside Comet</div><div class="price"><s>$10.00</s>$8.00</div><span class="btn">Add to Cart</span></div>
<div class="abs card-arr" style="left:611px;top:1528px"><div class="photo" role="img" aria-label="Pinball playfield artwork" style="background:linear-gradient(150deg,#3b4fa0,#c9a23a,#6a3a7a)"></div><div class="title">Flipside Comet</div><div class="price"><s>$10.00</s>$8.00</div><span class="btn">Add to Cart</span></div>
<div class="abs card-arr" style="left:863px;top:1528px"><div class="photo" role="img" aria-label="Pinball machine interior lit in blue" style="background:linear-gradient(150deg,#1a2a5a,#3a6ab0,#0e1630)"><span class="badge">Sale!</span></div><div class="title">Flipside Comet</div><div class="price"><s>$10.00</s>$8.00</div><span class="btn">Add to Cart</span></div>

<div class="abs pager" style="left:504px"><svg width="40" height="10" viewBox="0 0 40 10"><path d="M39 5H2M7 1L2 5l5 4" stroke="#fff" stroke-width="1.5" fill="none"/></svg></div>
<div class="abs pager" style="left:610px"><svg width="40" height="10" viewBox="0 0 40 10"><path d="M1 5h37M33 1l5 4-5 4" stroke="#fff" stroke-width="1.5" fill="none"/></svg></div>

<!-- blogs -->
<section class="abs blogs"></section>
<h2 class="abs section-head" style="top:1890px;color:#fff;font-size:30px;font-weight:400">Recent Blogs</h2>
<div class="abs rule" style="top:1932px;background:#fff;opacity:.7"></div>

<article class="abs blog" style="left:111px">
  <div class="photo" role="img" aria-label="Arcade room with purple lighting and pinball machines" style="background:linear-gradient(150deg,#7a3aa0,#c44ab0,#3a2a5a)"></div>
  <h3>Have Greater Tree Have Earth</h3>
  <p>Be so void whose green female sea, open i after our two spirit image unto moveth can't days, face ev ...</p>
  <div class="meta"><span>&#9719; Mar 21st 2017</span><span>&#9786; Henry</span></div>
</article>
<article class="abs blog" style="left:448px">
  <div class="photo" role="img" aria-label="Players gathered around a pinball machine" style="background:linear-gradient(150deg,#3a4a7a,#6a8ac0,#2a2a3a)"></div>
  <h3>Have Greater Tree Have Earth</h3>
  <p>Be so void whose green female sea, open i after our two spirit image unto moveth can't days, face ev ...</p>
  <div class="meta"><span>&#9719; Mar 21st 2017</span><span>&#9786; Henry</span></div>
</article>
<article class="abs blog" style="left:782px">
  <div class="photo" role="img" aria-label="Row of pinball machines at a game store" style="background:linear-gradient(150deg,#3a2a2a,#8a4a3a,#3a6a5a)"></div>
  <h3>Have Greater Tree Have Earth</h3>
  <p>Be so void whose green female sea, open i after our two spirit image unto moveth can't days, face ev ...</p>
  <div class="meta"><span>&#9719; Mar 21st 2017</span><span>&#9786; Henry</span></div>
</article>

<!-- social -->
<div class="abs social" style="left:454px" aria-label="Social link"></div>
<div class="abs social" style="left:539px" aria-label="Social link"></div>
<div class="abs social" style="left:623px" aria-label="Social link"></div>
<div class="abs social" style="left:708px" aria-label="Social link"></div>

<!-- footer -->
<footer class="abs footer"></footer>
<div class="abs footer-brand"><div class="mark"></div><div class="name">Bumper Vault Arcade</div></div>
<div class="abs footer-addr"><svg width="10" height="14" viewBox="0 0 10 14"><path d="M5 0a5 5 0 00-5 5c0 4 5 9 5 9s5-5 5-9a5 5 0 00-5-5z" fill="#333"/><circle cx="5" cy="5" r="2" fill="#eee"/></svg><span>It is a long established fact that a reader will be distracted by the</span></div>
<div class="abs footer-phone"><svg width="11" height="11" viewBox="0 0 24 24"><path fill="#222" d="M6.6 10.8a15 15 0 006.6 6.6l2.2-2.2c.3-.3.7-.4 1-.2 1.1.4 2.3.6 3.6.6.6 0 1 .4 1 1V20c0 .6-.4 1-1 1A17 17 0 013 4c0-.6.4-1 1-1h3.5c.6 0 1 .4 1 1 0 1.3.2 2.5.6 3.6.1.3 0 .7-.2 1z"/></svg>555-014-0199</div>

<div class="abs vline" style="left:365px"></div>
<div class="abs vline" style="left:587px"></div>
<div class="abs vline" style="left:877px"></div>

<div class="abs f-head" style="left:416px">Quick Links</div>
<ul class="abs f-list" style="left:405px;top:2392px">
  <li>&#8594; <span>Home</span></li><li>&#8594; <span>Shop</span></li><li>&#8594; <span>Blog</span></li><li>&#8594; <span>Page</span></li><li>&#8594; <span>Contact Us</span></li>
</ul>

<div class="abs f-head" style="left:624px">Blogs</div>
<div class="abs" style="left:624px;top:2400px">
  <div class="f-blog"><div class="thumb" role="img" aria-label="Blog thumbnail"></div><p>It is a long established fact that a reader will be distracted by the<small>22nd Mar 2017 &#9733;&#9733;&#9733;&#9733;</small></p></div>
  <div class="f-blog"><div class="thumb" role="img" aria-label="Blog thumbnail"></div><p>It is a long established fact that a reader will be distracted by the<small>22nd Mar 2017 &#9733;&#9733;&#9733;&#9733;</small></p></div>
  <div class="f-blog"><div class="thumb" role="img" aria-label="Blog thumbnail"></div><p>It is a long established fact that a reader will be distracted by the<small>22nd Mar 2017</small></p></div>
</div>

<div class="abs f-head" style="left:920px">Delivery &amp; Returns</div>
<ul class="abs f-list" style="left:910px;top:2392px">
  <li style="height:30px">&#8594; <span>Delivery</span></li><li style="height:30px">&#8594; <span>Order Tracking</span></li><li style="height:30px">&#8594; <span>Returns</span></li><li style="height:30px">&#8594; <span>E-Receipts</span></li><li style="height:30px">&#8594; <span>Buying Guides</span></li>
</ul>

<div class="abs basebar"></div>
</body>
</html>
```